Business card and insta posting square

This is for 2 separate projects...

1...a double sided business card for online business (no address) to hand to businesses to get them to list their details on my online directory. the butterfly logo is to be used on the business card.

2.... a posting square for Instagram to write inspirational quotes over the top of to post....with a small butterfly logo somewhere on it (in a corner maybe)....the square is to have a thin, solid green outline around the edge of it, and a faded picture through the background that will allow me to write text over the top of it that will be easily readable.
I would like the same box for all Instagram quote posts for consistency ..

Target Market(s)

spiritual , yoga, meditation, wellness......

Industry/Entity Type

Wellness

Contact Information for Business Card

Details for Business Card...
Tending A Bright Garden
Your Complete Wellness Directory
www.tendingabrightgarden.example
insta/FB/pinterest/twitter
*List Your Business for FREE *

Colors
33b8a4
34a7d8
3276b5
876aae
9bcb3c

Requirements
Must have
• butterfly logo included on business card
• insta post square can use the butterfly logo OR the TABG green square uploaded in the images
Nice to have
• greens

```html
<!DOCTYPE html>
<html lang="en">
<head>
<meta charset="utf-8">
<title>Tending A Bright Garden – Business Card</title>
<link href="https://fonts.googleapis.com/css2?family=Montserrat:wght@500;600;700&display=swap" rel="stylesheet">
<style>
  :root {
    --stage: #e9e9e7;
    --card-white: #ffffff;
    --green: #6cb33f;
    --green-dark: #3a9a3c;
    --teal: #1a9fae;
    --blue: #2c5fa8;
    --purple: #5b2a86;
    --ink-shadow: rgba(0, 0, 0, 0.18);
  }
  * { box-sizing: border-box; margin: 0; padding: 0; }
  html, body { width: 1200px; height: 900px; overflow: hidden; }
  body {
    background: var(--stage);
    font-family: "Montserrat", Arial, sans-serif;
    position: relative;
  }
  .card {
    position: absolute;
    width: 680px;
    height: 390px;
    border-radius: 4px;
    box-shadow: 0 10px 24px var(--ink-shadow);
    overflow: hidden;
  }
  /* Front side */
  .card--front {
    left: 440px;
    top: 40px;
    background: linear-gradient(155deg, var(--green) 0%, #3fae7a 25%, var(--teal) 45%, var(--blue) 72%, var(--purple) 100%);
    display: flex;
    flex-direction: column;
    align-items: center;
    justify-content: center;
    gap: 22px;
  }
  .front-mark {
    width: 96px;
    height: 96px;
    border-radius: 50%;
    background: rgba(255, 255, 255, 0.9);
  }
  .front-name {
    color: #ffffff;
    font-weight: 600;
    font-size: 34px;
    letter-spacing: 0.5px;
  }
  /* Back side */
  .card--back {
    left: 80px;
    top: 470px;
    background: var(--card-white);
    display: flex;
    align-items: center;
    padding: 0 32px 0 18px;
  }
  .brand-block {
    width: 250px;
    flex: none;
    display: flex;
    flex-direction: column;
    align-items: center;
    gap: 10px;
  }
  .brand-mark {
    width: 70px;
    height: 70px;
    border-radius: 50%;
    background: var(--purple);
  }
  .brand-name {
    color: var(--green-dark);
    font-weight: 600;
    font-size: 17px;
    white-space: nowrap;
  }
  .brand-tagline {
    color: var(--green-dark);
    font-weight: 600;
    font-size: 11.5px;
    white-space: nowrap;
  }
  .divider {
    width: 2px;
    height: 150px;
    flex: none;
    background: var(--purple);
    margin: 0 22px 0 14px;
  }
  .contact-block {
    display: flex;
    flex-direction: column;
    gap: 6px;
    color: var(--purple);
    min-width: 0;
  }
  .contact-block p { white-space: nowrap; }
  .person-name {
    font-weight: 700;
    font-size: 26px;
    line-height: 1;
  }
  .person-name .first { color: var(--purple); }
  .person-name .last { color: var(--teal); }
  .person-role {
    font-weight: 500;
    font-size: 17px;
    margin-bottom: 2px;
  }
  .social-handle {
    font-weight: 600;
    font-size: 14px;
    color: var(--teal);
  }
  .contact-line {
    display: flex;
    align-items: center;
    gap: 8px;
    font-weight: 500;
    font-size: 16px;
  }
  .contact-line svg { width: 17px; height: 17px; flex: none; }
  .cta {
    font-weight: 500;
    font-size: 16px;
  }
</style>
</head>
<body>
  <section class="card card--front" aria-label="Business card front">
    <div class="front-mark"></div>
    <p class="front-name">Tending A Bright Garden</p>
  </section>

  <section class="card card--back" aria-label="Business card back">
    <div class="brand-block">
      <div class="brand-mark"></div>
      <p class="brand-name">Tending A Bright Garden</p>
      <p class="brand-tagline">Your Complete Wellness Directory</p>
    </div>
    <div class="divider"></div>
    <div class="contact-block">
      <p class="person-name"><span class="first">Alex</span> <span class="last">Rivera</span></p>
      <p class="person-role">Manager</p>
      <p class="social-handle">@tendingabrightgarden</p>
      <p class="contact-line">
        <svg viewBox="0 0 24 24" aria-hidden="true"><path fill="#3a9a3c" d="M6.6 10.8a15 15 0 0 0 6.6 6.6l2.2-2.2a1 1 0 0 1 1-.25 11.4 11.4 0 0 0 3.6.57 1 1 0 0 1 1 1V20a1 1 0 0 1-1 1A17 17 0 0 1 3 4a1 1 0 0 1 1-1h3.5a1 1 0 0 1 1 1c0 1.25.2 2.450.57 3.57a1 1 0 0 1-.25 1z"/></svg>
        555-014-2100
      </p>
      <p class="contact-line">
        <svg viewBox="0 0 24 24" aria-hidden="true"><circle cx="12" cy="12" r="10" fill="none" stroke="#2c5fa8" stroke-width="2"/><path d="M2 12h20M12 2c3 3 3 17 0 20M12 2c-3 3-3 17 0 20" fill="none" stroke="#2c5fa8" stroke-width="1.6"/></svg>
        www.tendingabrightgarden.example
      </p>
      <p class="cta">List Your Business for FREE</p>
    </div>
  </section>
</body>
</html>
```